Recruitment Agency in Texas, needs a stand out header letter

Our colours are red and grey and can be found on our website
just my logo will be sufficient and address...

Target Market(s)

Engineering Manufacturing

Colors
0094D4
00A9DD
6FCCEA
C7EBF8
E9F6FB
EB3D1F
EC4F4E
F09395
F8D3D4
FCEDEE

Requirements
Must have
• use colors red and grey
Should not have
• Please use same colors and font as my logo. My website is kelbrantstaffing.net

```html
<!DOCTYPE html>
<html lang="en">
<head>
<meta charset="utf-8">
<title>Kelbrant Staffing Letterhead</title>
<link rel="stylesheet" href="https://fonts.googleapis.com/css2?family=Poppins:wght@400;500;600&family=Source+Sans+3:wght@700&display=swap">
<style>
  :root{
    --red:#ec2a2a;
    --grey:#6d6e72;
    --ink:#4a4a4d;
    --dark:#222226;
    --muted:#8a8a8e;
    --paper:#ffffff;
    --bg-top:#45c3c9;
    --bg-bottom:#14131b;
  }
  *{margin:0;padding:0;box-sizing:border-box}
  html,body{width:1200px;height:1200px;overflow:hidden}
  body{
    position:relative;
    background:linear-gradient(180deg,var(--bg-top) 0%,#3b7f80 45%,#232a31 75%,var(--bg-bottom) 100%);
    font-family:"Poppins",sans-serif;
  }
  .sheet-title{
    position:absolute;top:62px;left:0;width:1200px;text-align:center;
    font-family:"Source Sans 3",sans-serif;font-weight:700;font-size:25px;color:#fff;
    word-spacing:1px;
  }
  .page{
    position:absolute;left:266px;top:142px;width:667px;height:950px;background:var(--paper);
  }
  .edge-mark{position:absolute;left:0;top:0}
  .brand-name{
    position:absolute;left:32px;top:24px;font-weight:600;font-size:36px;color:var(--red);
    letter-spacing:-1px;line-height:1;
  }
  .contact-list{position:absolute;left:491px;top:15px;list-style:none}
  .contact-list li{display:flex;align-items:center;height:18.3px;font-size:11px;color:var(--ink)}
  .contact-list svg{width:9px;height:9px;margin-right:6px;fill:var(--red)}
  .office{position:absolute;left:491px;top:97px;font-size:11px;line-height:16px;color:var(--ink);font-weight:500}
  .office-label{color:var(--red);font-weight:600}
  .sender{position:absolute;left:20px;top:196px;color:var(--ink)}
  .sender-name{font-size:13.5px;font-weight:500;line-height:18px}
  .sender-role{font-size:11px;font-weight:500;line-height:16px}
  .sender-details{margin-top:9px;font-size:9px;line-height:16px}
  .sender-details b,.letter-date b{color:var(--red);font-weight:600}
  .letter-date{position:absolute;right:23px;top:270px;font-size:9px;color:var(--ink)}
  .letter-body{position:absolute;left:20px;top:342px;width:628px}
  .letter-body p{font-size:9px;line-height:14.7px;color:var(--muted);margin-bottom:14.5px}
  .letter-body p.emphasis{color:var(--dark)}
  .signature{
    position:absolute;left:23px;top:604px;width:146px;height:38px;
    background:linear-gradient(90deg,#fbe1e1,#fdf0f0);border-radius:4px;
  }
  .signature-rule{position:absolute;left:26px;top:654px;width:174px;border-top:1.5px dotted var(--dark)}
  .signer-name{position:absolute;left:24px;top:664px;font-size:16px;font-weight:600;color:var(--dark)}
  .signer-role{position:absolute;left:24px;top:688px;font-size:13px;font-weight:500;color:var(--red)}
  .footer-band{position:absolute;left:0;top:924px}
</style>
</head>
<body>
  <h1 class="sheet-title">Letterhead - Mockup 1 &nbsp;|&nbsp; Size - A44 &nbsp;|&nbsp; Color Mode - &nbsp;CMYK</h1>

  <div class="page">
    <svg class="edge-mark" width="22" height="98" viewBox="0 0 22 98">
      <rect x="0" y="0" width="11" height="97" fill="var(--red)"/>
      <polygon points="11,0 20,24 20,73 11,97" fill="var(--grey)"/>
    </svg>
    <div class="brand-name">Kelbrant Staffing</div>

    <ul class="contact-list">
      <li><svg viewBox="0 0 10 10"><path d="M2 0.5 3.6 2.6 2.8 3.8Q4 6.2 6.2 7.2L7.4 6.4 9.5 8 8.3 9.5Q4.5 9.4 1.4 5.6 0.3 3.6 0.6 1.6Z"/></svg>(+1) 713-555-0148</li>
      <li><svg viewBox="0 0 10 10"><rect x="0.5" y="2" width="9" height="7.5"/><rect x="2.3" y="0.5" width="5" height="3" fill="#fff" stroke="var(--red)" stroke-width="0.8"/></svg>713-555-0149</li>
      <li><svg viewBox="0 0 10 10"><path d="M0.5 2h9v6.5h-9z"/><path d="M0.8 2.3 5 5.6 9.2 2.3" stroke="#fff" stroke-width="0.9" fill="none"/></svg>info@kelbrantstaffing.net</li>
      <li><svg viewBox="0 0 10 10"><circle cx="5" cy="5" r="4.5"/><path d="M0.5 5h9M5 0.5v9M2 2.5h6M2 7.5h6" stroke="#fff" stroke-width="0.7"/></svg>www.kelbrantstaffing.net</li>
    </ul>

    <div class="office">
      <div class="office-label">Houston Office</div>
      <div>48 Larkfield Plaza Houston</div>
    </div>

    <div class="sender">
      <div class="sender-name">Owen Hartley</div>
      <div class="sender-role">Chief Executive Officer</div>
      <div class="sender-details">
        <div><b>A:</b> 57 Merrow Lane, CA, USA 100234</div>
        <div><b>P:</b> +91 90000 11122, +91 90000 33344</div>
        <div><b>W:</b> hello@brindlework.com, www.brindlework.com</div>
      </div>
    </div>
    <div class="letter-date"><b>Date:</b> 06-08-2021</div>

    <div class="letter-body">
      <p>Lorem ipsum dolor sit amet, consectetur adipiscing elit. Pellentesque dictum, ante non ullamcorp er convallis, nunc quam blandit metus, ac mollis eros felis a orci. Donec congue, mauris ut pulvinar lobortis, dolor massa feugiat nisi, at tincidunt metus leo vel elit.</p>
      <p>Nulla egestas vulputate risus, ut vestibulum diam commodo id. Mauris ornare libero eu erat portt itor ultrices. Proin sed lectus scelerisque ligula bibendum sagittis ac nec leo. Donec ac accumsan diam, et lobortis mauris. Nulla congue volutpat nisl ac lobortis.</p>
      <p class="emphasis">Nulla congue volutpat nisl ac lobortis. Integer dignissim interdum libero, quis feugiat velit pretium at. Phasellus sit amet libero rutrum, feugiat odio et, tempus purus. Cras ultricies, leo at fringilla solli cit udin, leo sapien placerat enim, a rutrum lorem enim ut tortor. Phasellus magna ante, cong ue maximus egestas sit amet, venenatis scelerisque felis.</p>
      <p>Nulla congue volutpat nisl ac lobortis. Integer dignissim interdum libero, quis feugiat velit pretium at. Phasellus sit amet libero rutrum, feugiat odio et, tempus purus. Cras ultricies, leo at fringilla solli cit udin, leo sapien placerat enim, a rutrum lorem enim ut tortor. Phasellus magna ante, cong ue maximus egestas sit amet, venenatis scelerisque felis</p>
    </div>

    <div class="signature" role="img" aria-label="Handwritten signature of Owen Hartley in red ink"></div>
    <div class="signature-rule"></div>
    <div class="signer-name">Owen Hartley</div>
    <div class="signer-role">Director</div>

    <svg class="footer-band" width="667" height="9" viewBox="0 0 667 9">
      <g fill="var(--red)">
        <polygon points="0,0 60,0 57,9 0,9"/>
        <polygon points="71,0 90,0 87,9 68,9"/>
        <polygon points="100,0 119,0 116,9 97,9"/>
        <polygon points="128,0 530,0 533,9 125,9"/>
        <polygon points="546,0 565,0 568,9 549,9"/>
        <polygon points="576,0 595,0 598,9 579,9"/>
        <polygon points="605,0 667,0 667,9 608,9"/>
      </g>
    </svg>
  </div>
</body>
</html>
```